Rooted Ready Rising: Quiet Roots, Open Doors, Steady Hands

I want a modern and clean looking book cover. 5.25x8

Title
Rooted Ready Rising

Subtitle
Quiet Roots, Open Doors, Steady Hands

I don’t just want a graphic, I want it to make sense. If it can just be the words and a textured looking background, I’ll be ok with that too. I just want it to look crisp, clean, modern.

I want the back to have my book blurb and bio attached with the pic that’s attached.

Target Market(s)

Self help

Requirements
Must have
• Modern, clean look, look professional, attract customers.

```html
<!DOCTYPE html>
<html lang="en">
<head>
<meta charset="utf-8">
<title>Rooted Ready Rising — Book Cover</title>
<link rel="stylesheet" href="https://fonts.googleapis.com/css2?family=Jost:wght@300;400&display=swap">
<style>
  :root {
    --stone: #b3ada6;
    --stone-deep: #a39d96;
    --ink-light: #ffffff;
    --rule: rgba(255, 255, 255, 0.88);
  }
  html, body {
    margin: 0;
    padding: 0;
    width: 788px;
    height: 1200px;
    overflow: hidden;
    background: var(--stone);
  }
  .cover {
    position: relative;
    width: 788px;
    height: 1200px;
    overflow: hidden;
    background: radial-gradient(ellipse at 50% 45%, var(--stone) 0%, var(--stone-deep) 100%);
    font-family: "Jost", "Century Gothic", sans-serif;
    color: var(--ink-light);
  }
  .cover-texture,
  .cover-rules {
    position: absolute;
    inset: 0;
    width: 788px;
    height: 1200px;
  }
  .author {
    position: absolute;
    top: 30px;
    left: 0;
    width: 100%;
    text-align: center;
    font-weight: 400;
    font-size: 19px;
    letter-spacing: 0.5px;
  }
  .title-word {
    position: absolute;
    left: 0;
    width: 100%;
    text-align: center;
    font-weight: 300;
    font-size: 74px;
    line-height: 1;
    letter-spacing: -0.5px;
  }
  .title-word--first  { top: 258px; }
  .title-word--second { top: 384px; }
  .title-word--third  { top: 528px; }
  .subtitle {
    position: absolute;
    top: 988px;
    left: 0;
    width: 100%;
    text-align: center;
    font-weight: 300;
    font-size: 18px;
    letter-spacing: 0.3px;
  }
</style>
</head>
<body>
  <main class="cover">
    <svg class="cover-texture" viewBox="0 0 788 1200" aria-hidden="true">
      <filter id="grain">
        <feTurbulence type="fractalNoise" baseFrequency="0.9" numOctaves="3" stitchTiles="stitch"/>
        <feColorMatrix type="saturate" values="0"/>
        <feComponentTransfer>
          <feFuncA type="linear" slope="0.18"/>
        </feComponentTransfer>
      </filter>
      <rect width="788" height="1200" filter="url(#grain)"/>
    </svg>

    <svg class="cover-rules" viewBox="0 0 788 1200" aria-hidden="true">
      <g stroke="var(--rule)" stroke-width="1.6">
        <line x1="197" y1="252" x2="605" y2="252"/>
        <line x1="197" y1="259" x2="605" y2="259"/>
        <line x1="197" y1="265" x2="605" y2="265"/>
        <line x1="197" y1="272" x2="605" y2="272"/>
        <line x1="197" y1="278" x2="605" y2="278"/>
        <line x1="197" y1="285" x2="605" y2="285"/>
        <line x1="197" y1="326" x2="605" y2="326"/>
        <line x1="197" y1="368" x2="605" y2="368"/>
        <line x1="197" y1="410" x2="605" y2="410"/>
        <line x1="197" y1="454" x2="605" y2="454"/>
        <line x1="197" y1="496" x2="605" y2="496"/>
        <line x1="197" y1="540" x2="605" y2="540"/>
        <line x1="197" y1="596" x2="605" y2="596"/>
        <line x1="197" y1="640" x2="605" y2="640"/>
      </g>
    </svg>

    <p class="author">Mara Ellison</p>

    <h1 class="title">
      <span class="title-word title-word--first">Rooted</span>
      <span class="title-word title-word--second">Ready</span>
      <span class="title-word title-word--third">Rising</span>
    </h1>

    <p class="subtitle">Quiet Roots, Open Doors, Steady Hands</p>
  </main>
</body>
</html>
```